IT company requires website redesign

I have an old boring website that I want to update - www.tlvx-example.com
I am a growing IT company beginning to look after more healthcare professionals such as medical and dental practices so a more professional look is required

Blue and orange are the company colours. See one of our local competitors for your reference and ideas - https://www.pixel-helpdesk.example.au

Target Market(s)

Medical, dental, professional, solicitors etc

Industry/Entity Type

It Support

Number of Pages Required

5+ page

Colors

Designer to choose colors to be used in the design.

Requirements
Must have
• Classy feel, simple with the 'less is more' approach
• On support page, links to support items, a couple more to come
• Reference to our technology partners
• Easy to read
Nice to have
• Company colours are blue with a little orange but I willing to consider new web colour schemes
• leave the rest to you

```html
<!DOCTYPE html>
<html lang="en">
<head>
<meta charset="utf-8">
<title>Quillrest IT – Contact Us</title>
<link rel="stylesheet" href="https://fonts.googleapis.com/css2?family=Jost:wght@400;500&family=Open+Sans:wght@400;600&family=Arimo:wght@400&display=swap">
<style>
  :root {
    --brand-blue: #1a56a8;
    --brand-blue-deep: #1552a0;
    --brand-orange: #ec6a2a;
    --ink: #1b1b1b;
    --muted: #9a9a9a;
    --field-border: #c9c9c9;
    --hero-grey: #dddde0;
    --footer-dark: #242424;
    --white: #ffffff;
  }
  * { box-sizing: border-box; margin: 0; padding: 0; }
  html, body { width: 785px; height: 1200px; overflow: hidden; background: var(--white); }
  body { position: relative; font-family: "Open Sans", sans-serif; color: var(--ink); }

  .site-header { position: absolute; top: 0; left: 0; width: 785px; height: 54px; background: var(--white); }
  .brand { position: absolute; left: 86px; top: 20px; display: flex; align-items: center; gap: 6px;
           font-family: "Jost", sans-serif; font-weight: 500; font-size: 13px; color: var(--brand-blue); }
  .brand-dot { width: 9px; height: 9px; border-radius: 50%; background: var(--brand-orange); }
  .main-nav { position: absolute; right: 80px; top: 25px; display: flex; gap: 22px;
              font-family: "Arimo", sans-serif; font-size: 8.5px; }
  .main-nav a { color: var(--ink); text-decoration: none; }
  .main-nav a.is-active { color: var(--brand-orange); }

  .hero { position: absolute; top: 54px; left: 0; width: 785px; height: 224px; background: var(--hero-grey); }
  .hero-title { position: absolute; left: 83px; top: 62px; font-family: "Jost", sans-serif; font-weight: 400;
                font-size: 24px; line-height: 26px; color: #2e2e2e; text-transform: uppercase; letter-spacing: 0.2px; }
  .hero-compass { position: absolute; left: 458px; top: 20px; width: 206px; height: 188px;
                  background: radial-gradient(circle, #8a4a2a 0%, #2a3a3a 35%, #d6d6d9 70%); border-radius: 50%; opacity: .85; }

  .location-map { position: absolute; top: 278px; left: 0; width: 785px; height: 168px;
                  background: linear-gradient(135deg, #efe4cf 0%, #e8e2d6 45%, #d7e3c8 100%); }

  .contact-title { position: absolute; top: 487px; width: 785px; text-align: center;
                   font-family: "Jost", sans-serif; font-size: 18px; font-weight: 400; color: var(--ink); }
  .contact-title span { color: var(--brand-orange); }

  .field { position: absolute; height: 26px; border: 1px solid var(--field-border); background: var(--white);
           font-size: 7.5px; color: var(--muted); padding: 8px 6px; }
  .field-left { left: 232px; width: 154px; }
  .field-right { left: 399px; width: 154px; }
  .field-message { left: 232px; top: 651px; width: 320px; height: 89px; }
  .submit-btn { position: absolute; left: 342px; top: 757px; width: 101px; height: 26px; background: var(--brand-blue);
                color: var(--white); font-family: "Jost", sans-serif; font-size: 11px; font-weight: 500;
                display: flex; align-items: center; justify-content: center; }

  .contact-item { position: absolute; top: 836px; display: flex; align-items: flex-end; gap: 8px; }
  .contact-item svg { width: 12px; height: 14px; }
  .contact-label { font-size: 5px; color: var(--muted); margin-bottom: 4px; }
  .contact-value { font-size: 8.5px; color: var(--ink); }

  .help-band { position: absolute; top: 908px; left: 0; width: 785px; height: 167px;
               background: linear-gradient(160deg, #1d5aab 0%, var(--brand-blue-deep) 60%, #1b57a5 100%); text-align: center; }
  .help-title { margin-top: 44px; font-family: "Jost", sans-serif; font-size: 17px; font-weight: 400; color: var(--white); }
  .help-title span { color: var(--brand-orange); }
  .help-sub { margin-top: 6px; font-family: "Jost", sans-serif; font-size: 10.5px; font-weight: 500; color: var(--white); }
  .help-btn { display: inline-flex; align-items: center; justify-content: center; margin-top: 28px; width: 101px; height: 26px;
              background: var(--white); color: var(--brand-blue); font-family: "Jost", sans-serif; font-size: 11px; font-weight: 400; }

  .site-footer { position: absolute; top: 1075px; left: 0; width: 785px; height: 125px; background: var(--footer-dark); }
  .footer-nav { position: absolute; top: 21px; width: 785px; display: flex; justify-content: center; gap: 22px;
                font-family: "Arimo", sans-serif; font-size: 8.5px; }
  .footer-nav a { color: var(--white); text-decoration: none; }
  .footer-nav a.is-active { color: var(--brand-orange); }
  .footer-contact { position: absolute; top: 50px; width: 785px; text-align: center; font-family: "Arimo", sans-serif;
                    font-size: 8px; color: var(--brand-orange); }
  .social-row { position: absolute; top: 68px; width: 785px; display: flex; justify-content: center; gap: 7px; }
  .social-row span { width: 13px; height: 13px; background: var(--white); border-radius: 2px; }
  .footer-rule { position: absolute; top: 101px; left: 0; width: 785px; height: 1px; background: #333; }
  .copyright { position: absolute; top: 109px; width: 785px; text-align: center; font-size: 5.5px; color: #8a8a8a; }
</style>
</head>
<body>
  <header class="site-header">
    <div class="brand"><span class="brand-dot"></span>Quillrest IT</div>
    <nav class="main-nav">
      <a href="#">Home</a><a href="#">Our Services</a><a href="#">About Us</a>
      <a href="#" class="is-active">Our Team</a><a href="#">Contact Us</a><a href="#">Support</a>
    </nav>
  </header>

  <section class="hero">
    <h1 class="hero-title">A clearer path forward,<br>guided by smart<br>technology choices today</h1>
    <div class="hero-compass" role="img" aria-label="Compass rose illustration with north, east, south and west markers"></div>
  </section>

  <div class="location-map" role="img" aria-label="Street map showing the office location"></div>

  <h2 class="contact-title">Contact <span>Us</span></h2>
  <div class="field field-left" style="top:538px">Select doctor</div>
  <div class="field field-right" style="top:538px">Select Time</div>
  <div class="field field-left" style="top:576px">Your Name</div>
  <div class="field field-right" style="top:576px">Phone</div>
  <div class="field field-left" style="top:614px">Your Email</div>
  <div class="field field-right" style="top:614px">11/11/1111</div>
  <div class="field field-message">Your Message*</div>
  <div class="submit-btn">Submit</div>

  <div class="contact-item" style="left:173px">
    <svg viewBox="0 0 12 14"><rect x="2.5" y="1" width="7" height="12" rx="1.5" fill="none" stroke="#ec6a2a" stroke-width="1.3"/><line x1="5" y1="11" x2="7" y2="11" stroke="#ec6a2a" stroke-width="1"/></svg>
    <div><div class="contact-label">Give us a Call</div><div class="contact-value">1300 482 617</div></div>
  </div>
  <div class="contact-item" style="left:337px">
    <svg viewBox="0 0 14 14"><rect x="1" y="3" width="12" height="8" fill="none" stroke="#ec6a2a" stroke-width="1.3"/><polyline points="1,3 7,8 13,3" fill="none" stroke="#ec6a2a" stroke-width="1.2"/></svg>
    <div><div class="contact-label">Send us a Message</div><div class="contact-value">info@tlvx-example.com</div></div>
  </div>
  <div class="contact-item" style="left:503px">
    <svg viewBox="0 0 12 14"><path d="M6 13 C2 8 1.5 6.5 1.5 5 A4.5 4.5 0 0 1 10.5 5 C10.5 6.5 10 8 6 13Z" fill="none" stroke="#ec6a2a" stroke-width="1.2"/><circle cx="6" cy="5" r="1.6" fill="none" stroke="#ec6a2a" stroke-width="1"/></svg>
    <div><div class="contact-label">Visit our Location</div><div class="contact-value">12 Harbour Lane, Coastview QLD 4999</div></div>
  </div>

  <section class="help-band">
    <h2 class="help-title"><span>Quillrest IT -</span> We Are Here To Help You</h2>
    <p class="help-sub">A Clearer Path Forward, Guided by Smart Technology Choices Today!</p>
    <div class="help-btn">Contact Us</div>
  </section>

  <footer class="site-footer">
    <nav class="footer-nav">
      <a href="#" class="is-active">Home</a><a href="#">Our Services</a><a href="#">About Us</a>
      <a href="#">Our Team</a><a href="#">Contact Us</a><a href="#">Support</a>
    </nav>
    <div class="footer-contact">1300-482-617 | info@tlvx-example.com</div>
    <div class="social-row"><span></span><span></span><span></span><span></span><span></span></div>
    <div class="footer-rule"></div>
    <div class="copyright">QUILLRESTIT-2019 / All Rights Reserved</div>
  </footer>
</body>
</html>
```